new signage design for budget motel - Brookfern Lodge

renaming the budget motel as Brookfern Lodge, property located on side of a hill. therefore i choose to name is Brookfern Lodge, im looking for clean, modern look in signage design,this property does not have a Logo, plan to us signage design as a logo as well. current pole sign housing is rectangle shape and will be using same housing I'll be attaching picture of the signage for better idea. looking forward to awesome creative designs.

Industry/Entity Type

Motel

Font styles to use
Serif
Sans Serif

Requirements
Should not have
• mountains , mountain(s) with snow , trees, no black color, red color, blue letters, too much green.

```html
<!DOCTYPE html>
<html lang="en">
<head>
<meta charset="utf-8">
<title>Brookfern Lodge Motel Sign</title>
<link rel="stylesheet" href="https://fonts.googleapis.com/css2?family=Open+Sans:wght@600;700&family=Crimson+Pro:wght@700&display=swap">
<style>
  :root {
    --sign-bg: #efebe6;
    --frame-green: #00703c;
    --brand-gold: #c3841c;
    --band-gold: #cf9021;
    --motel-brown: #6e3a22;
    --page-white: #ffffff;
  }
  html, body {
    margin: 0;
    padding: 0;
    width: 1200px;
    height: 473px;
    overflow: hidden;
    background: var(--page-white);
  }
  .sign {
    position: relative;
    width: 1200px;
    height: 473px;
  }
  .sign-panel {
    position: absolute;
    left: 15px;
    top: 15px;
    width: 1170px;
    height: 443px;
    background: var(--sign-bg);
  }
  .sign-frame {
    position: absolute;
    left: 23px;
    top: 23px;
    width: 1146px;
    height: 419px;
    border: 4px solid var(--frame-green);
  }
  .brand-art {
    position: absolute;
    left: 0;
    top: 0;
    width: 1200px;
    height: 473px;
  }
  .brand-name {
    font-family: "Open Sans", sans-serif;
    font-weight: 700;
    font-size: 124px;
    fill: var(--brand-gold);
  }
  .brand-band {
    fill: var(--band-gold);
  }
  .motel-label {
    position: absolute;
    right: 68px;
    top: 268px;
    margin: 0;
    font-family: "Open Sans", sans-serif;
    font-weight: 600;
    font-size: 106px;
    line-height: 1;
    letter-spacing: 4px;
    color: var(--motel-brown);
  }
  .call-line {
    position: absolute;
    left: 72px;
    top: 330px;
    margin: 0;
    font-family: "Crimson Pro", serif;
    font-weight: 700;
    font-size: 56px;
    line-height: 1;
    color: var(--motel-brown);
  }
</style>
</head>
<body>
  <div class="sign">
    <div class="sign-panel"></div>
    <div class="sign-frame"></div>

    <svg class="brand-art" viewBox="0 0 1200 473" aria-label="Brookfern Lodge">
      <text class="brand-name" x="70" y="205" textLength="1060" lengthAdjust="spacing">Brookfern Lodge</text>
      <rect class="brand-band" x="70" y="246" width="1060" height="10"/>
    </svg>

    <p class="motel-label">MOTEL</p>
    <p class="call-line">Call - 0000000000</p>
  </div>
</body>
</html>
```